Avocado Smoothies (100% Natural, No Preservatives, No added Sugar)

We need a company logo (for business cards etc) as well as label design (front and back) for a range of avocado based smoothies on our 300 ml bottle & pouch with drinking spout. The look & feel of the label is that the smoothies are fresh & healthy, prepared with freshest ingredients & formulated with nutritional needs in mind.

The final design should give the impression of a genuine & trusted brand of beverage that is appealing to (1) health conscious busy professionals both male & female (e.g. gym / yoga / athletic buffs), (2) busy mothers of fussy / picky kids; and (3) people who like more plant-based diets, who want the best products for them / their families. The design is to be innovative & appealing to the intelligent health conscious consumers especially avocado fans, looking for healthier alternatives of natural drinks on-the go, that are NOT prepared by big, impersonal & highly automated factories that use all sorts of nasties & processes in their beverages. Easy to read FONT and preferably include an original picture of avocado (which can be a real picture / graphic design) - however, this is not necessary.

Company name: OKUN Pte.Ltd. (the letter "I" may mean "I" or "Innovative" or "Intelligent". "OKUN" can be a play of the word "I ever .... " e.g. "all OKUN wanted is ... ".)

Please note that the master label design should be versatile enough for a range of avocado smoothies (we only need to make minimum changes to the main picture / words as necessary for each specific avocado smoothie) and the label can also be used for kids size and adult size pouches and bottles of height 16cm and diameter of circular base of 5.5cm.

Target Market(s)

(1) health conscious busy professionals (e.g. gym / yoga / athletic buffs), (2) busy mothers of fussy / picky kids; and (3) vegans & people who like more plant based diets, who want the best products for them / their families.

Logo Text

OKUN

Font styles to use
Serif
Sans Serif
Decorative
Script

Colors

Designer to choose colors to be used in the design.

Requirements
Must have
• Centre attention of the label (BIG font): Avocado & [we insert the other main ingredients] Smoothie
• Company logo (noticeable somewhere on the label): OKUN
• (Medium font) All natural ingredients, no added sugar or salt, no additives or preservatives
• (Smaller fonts) Along the lines of: "Made from the finest blend of avocados and [we can insert other ingredients] to nourish you. Rich, creamy, wholesome & unique avocado experience that is good and satisfyingly delicious! "
• Keep refrigerated below 5 deg C
• Manufactured by: [we insert details]
• 300ml
Nice to have
• Please recycle usual logo
• originality & fresh & appealing factor
Should not have
• unhealthy image / junk food / sugary / additives / unsavoury impression
• difficult to read font
• confusion with other existing brands

```html
<!DOCTYPE html>
<html lang="en">
<head>
<meta charset="utf-8">
<title>OKUN Avocado Smoothies – Front Label</title>
<link href="https://fonts.googleapis.com/css2?family=Questrial&display=swap" rel="stylesheet">
<style>
  :root {
    --backdrop: #fbee5c;
    --label-bg: #e5e5e3;
    --label-edge: #d6d6d3;
    --ink: #141414;
    --leaf-green: #7cc232;
    --white: #ffffff;
    --avo-dark: #4f9a24;
    --avo-light: #a9d24a;
  }
  * { margin: 0; padding: 0; box-sizing: border-box; }
  html, body {
    width: 1200px; height: 900px; overflow: hidden;
    background: var(--backdrop);
    font-family: "Questrial", sans-serif;
    color: var(--ink);
  }
  .canvas { position: relative; width: 1200px; height: 900px; }
  .label {
    position: absolute; left: 414px; top: 172px;
    width: 376px; height: 596px;
    background: var(--label-bg);
    border: 1px solid var(--label-edge);
  }
  .brand-name {
    position: absolute; left: 0; right: 0; top: 72px;
    text-align: center;
    font-size: 82px; font-weight: 400; line-height: 1; letter-spacing: 5px;
    color: var(--ink);
  }
  .product-title {
    position: absolute; left: 0; right: 0; top: 158px;
    text-align: center; font-size: 26px; font-weight: 400; letter-spacing: 1.5px;
  }
  .product-blurb {
    position: absolute; left: 40px; right: 28px; top: 192px;
    text-align: center; font-size: 6.6px; line-height: 1.35;
  }
  .hero-fruit {
    position: absolute; left: 62px; top: 232px;
    width: 256px; height: 236px;
    border-radius: 24px;
    background: linear-gradient(135deg, var(--avo-light) 0%, var(--avo-dark) 100%);
  }
  .range-band {
    position: absolute; right: 0; top: 254px;
    width: 50px; height: 326px;
    background: var(--leaf-green);
    border-radius: 10px 0 0 0;
    display: flex; align-items: center; justify-content: center;
  }
  .range-band span {
    transform: rotate(-90deg);
    white-space: nowrap;
    font-size: 42px; letter-spacing: 2px;
    color: var(--white);
  }
  .natural-claim {
    position: absolute; left: 6px; right: 0; top: 486px;
    text-align: center; font-size: 13px; letter-spacing: 0.6px;
  }
  .free-from {
    position: absolute; left: 6px; right: 0; top: 510px;
    display: flex; justify-content: center; gap: 14px;
  }
  .free-from figure { width: 26px; text-align: center; }
  .free-from svg { width: 20px; height: 20px; display: block; margin: 0 auto; }
  .free-from figcaption { font-size: 3.6px; margin-top: 2px; white-space: nowrap; }
  .blend-note {
    position: absolute; left: 6px; right: 0; top: 548px;
    text-align: center; font-size: 7px; letter-spacing: 0.3px;
  }
</style>
</head>
<body>
<main class="canvas">
  <section class="label">
    <h1 class="brand-name">OKUN</h1>
    <h2 class="product-title">Avocado &amp;</h2>
    <p class="product-blurb">Lorem ipsum dolor sit amet, consectetuer adipiscing elit, sed diam nonummy<br>nibh euismod tincidunt ut laoreet dolore magna aliquam erat volutpat.</p>

    <div class="hero-fruit" role="img" aria-label="Illustration of a whole green avocado beside a halved avocado with its stone and a leaf"></div>

    <div class="range-band"><span>SMOOTHIES</span></div>

    <p class="natural-claim">All natural ingredients</p>

    <div class="free-from">
      <figure>
        <svg viewBox="0 0 20 20" fill="none" stroke="#141414" stroke-width="1.2">
          <circle cx="10" cy="10" r="8.6"/>
          <rect x="6.5" y="7" width="6" height="6"/>
          <line x1="4" y1="4" x2="16" y2="16"/>
        </svg>
        <figcaption>No Sugar</figcaption>
      </figure>
      <figure>
        <svg viewBox="0 0 20 20" fill="none" stroke="#141414" stroke-width="1.2">
          <circle cx="10" cy="10" r="8.6"/>
          <path d="M7.5 14 L8 8 Q10 5 12 8 L12.5 14 Z"/>
          <line x1="4" y1="4" x2="16" y2="16"/>
        </svg>
        <figcaption>No Salt</figcaption>
      </figure>
      <figure>
        <svg viewBox="0 0 20 20" fill="none" stroke="#141414" stroke-width="1.2">
          <circle cx="10" cy="10" r="8.6"/>
          <path d="M8.5 5 V9 L6 14 H14 L11.5 9 V5"/>
          <line x1="4" y1="4" x2="16" y2="16"/>
        </svg>
        <figcaption>No Preservatives</figcaption>
      </figure>
    </div>

    <p class="blend-note">Made from the finest blend of avocados and</p>
  </section>
</main>
</body>
</html>
```